Cat-products company needs smart, yet endearing, business card

We need a business card design for a new, but up-and-running, business based in Honolulu, Hawaii. The business is Purrlane Nest Co. Our first product is the most environmentally-friendly cat grass kit ever seen on the planet. Future products, currently in the R&D phase, will include a variety of exciting cat scratchers. We also do consulting work to help apartment-dwellers make their home more cat-friendly and, in the future, plan on doing full, custom installs of structure to create high walkways for cats.

Target Market(s)

Middle-aged, apartment-dwelling, middle-class workers who own 1 or more cats and who dote on them.

Industry/Entity Type

Pet Care

Contact Information for Business Card

A striking, professional, yet warm and friendly design is what we're after.

Font styles to use
Serif
Sans Serif
Other font styles liked:
• Comfortaa

Colors

Designer to choose colors to be used in the design.

Requirements
Must have
• The company logo: (see attachment)
• The company name: Purrlane Nest Co
• The web address: www.purrlanenestco.example
• Email: support@purrlanenestco.example
• Phone: +1 (808) 574 1630
• Update (Fri Jun 30 3017 7:45pm Hawaii Time) I would like, is possible, uploaded picture of the cat grass kit on the back of the card with some text along the lines of: Purrlane Nest Co - Maker Of The Freshest Cat Grass Kit Yet
Nice to have
• A cat picture, cartoon, real or silhouette that illustrates cats in action and/or relaxing; ie using the apartment space to live, play and relax in and being well-contented.
• Most of the website is done in the font: Comfortaa. It might be nice to continue using this for brand consistency.
Should not have
• Hard-to-read fonts.

```html
<!DOCTYPE html>
<html lang="en">
<head>
<meta charset="UTF-8">
<title>Purrlane Nest Co — Business Card</title>
<link rel="stylesheet" href="https://fonts.googleapis.com/css2?family=Open+Sans:wght@400;600;700&display=swap">
<style>
  :root {
    --backdrop: #2b2b2b;
    --card-white: #ffffff;
    --brand-brown: #5a3526;
    --brand-yellow: #fbb615;
    --ink: #1f1f1f;
  }
  * { margin: 0; padding: 0; box-sizing: border-box; }
  html, body {
    width: 1200px;
    height: 685px;
    overflow: hidden;
    background: var(--backdrop);
    font-family: "Open Sans", Arial, sans-serif;
  }
  .sheet {
    position: relative;
    width: 1200px;
    height: 685px;
    display: flex;
    align-items: center;
    justify-content: center;
    gap: 40px;
  }
  .card {
    position: relative;
    width: 520px;
    height: 297px;
    background: var(--card-white);
    overflow: hidden;
    box-shadow: 0 10px 30px rgba(0,0,0,0.45);
  }
  /* Front face */
  .brand-name {
    position: absolute;
    top: 34px;
    left: 34px;
    display: flex;
    align-items: center;
    gap: 10px;
    font-weight: 700;
    font-size: 22px;
    color: var(--brand-brown);
    letter-spacing: 0.2px;
  }
  .brand-dot {
    width: 18px;
    height: 18px;
    background: var(--brand-yellow);
  }
  .contact {
    position: absolute;
    left: 34px;
    top: 160px;
    font-size: 15px;
    line-height: 22px;
    color: var(--ink);
  }
  .web-band {
    position: absolute;
    left: 0;
    right: 0;
    top: 215px;
    height: 32px;
    background: var(--brand-yellow);
    display: flex;
    align-items: center;
    padding-left: 34px;
  }
  .web-band .website {
    font-size: 18px;
    font-weight: 600;
    color: var(--brand-brown);
    letter-spacing: 0.3px;
  }
  /* Back face */
  .card--back {
    display: flex;
    align-items: center;
    justify-content: center;
  }
  .back-name {
    font-weight: 700;
    font-size: 26px;
    color: var(--brand-brown);
  }
</style>
</head>
<body>
  <main class="sheet">
    <section class="card card--front" aria-label="Business card front">
      <div class="brand-name"><span class="brand-dot"></span><span>Purrlane Nest Co</span></div>
      <div class="contact">
        <p class="phone">+1 (808) 574 1630</p>
        <p class="email">support@purrlanenestco.example</p>
      </div>
      <div class="web-band">
        <span class="website">www.purrlanenestco.example</span>
      </div>
    </section>

    <section class="card card--back" aria-label="Business card back">
      <span class="back-name">Purrlane Nest Co</span>
    </section>
  </main>
</body>
</html>
```